Brochure - Silver Harbor Circle

We need a brochure (tri-fold or bi-fold) for our network marketing company, Silver Harbor Circle. The brochure will be used for our Promoters (Distributors) to hand out to prospective customers and Promoters explaining our service as well as the income opportunity.

Industry/Entity Type

Club

```html
<!DOCTYPE html>
<html lang="en">
<head>
<meta charset="utf-8">
<title>Silver Harbor Circle – Brochure</title>
<link href="https://fonts.googleapis.com/css2?family=Roboto+Condensed:wght@700&family=Roboto:wght@300;400;500;700&display=swap" rel="stylesheet">
<style>
:root{
  --blue:#1f9be0;
  --green:#7cc242;
  --green-dark:#5fa52c;
  --grey-text:#555;
  --grey-light:#ececec;
  --pill:#e2e2e2;
  --page:#f7f7f7;
  --bg:#d9d4cc;
}
*{box-sizing:border-box;margin:0;padding:0}
html,body{width:1200px;height:1200px;overflow:hidden}
body{background:var(--bg);font-family:"Roboto",Arial,sans-serif;color:var(--grey-text);position:relative}
.spread{position:absolute;left:230px;width:740px;height:570px;display:grid;grid-template-columns:repeat(3,1fr);box-shadow:0 4px 14px rgba(0,0,0,.25);background:#fff}
.spread--outside{top:20px}
.spread--inside{top:610px}
.panel{position:relative;overflow:hidden}
.brand{font-family:"Roboto Condensed",Arial,sans-serif;font-weight:700;color:var(--blue);line-height:1;display:flex;align-items:center;gap:6px}
.brand-dot{width:10px;height:10px;border-radius:50%;background:var(--green);flex:none}
.brand-sub{font-weight:300;color:var(--grey-text);font-size:12px;text-align:right;margin-top:2px}

/* Outside: services panel */
.services{background:#fff}
.pill{margin-top:22px;width:205px;height:28px;background:var(--pill);border-radius:0 14px 14px 0;font-weight:500;font-size:16px;letter-spacing:.5px;color:var(--grey-text);padding:4px 0 0 16px}
.service{padding:10px 36px 0 0;display:flex;flex-direction:column;align-items:flex-end}
.service .brand{font-size:22px}
.sunset-photo{position:absolute;left:0;right:0;bottom:0;height:250px;background:linear-gradient(170deg,#fdf6e6 0%,#f3c98a 30%,#b58a62 60%,#5a4a40 100%)}
.seal{position:absolute;width:82px;height:82px;border-radius:50%;background:#3a3a3a;border:3px solid #fff;box-shadow:0 0 0 2px #3a3a3a}
.services .seal{left:92px;top:335px}

/* Contact panel */
.contact{background:#f2f2f2}
.contact-frame{position:absolute;left:16px;right:18px;top:28px;bottom:14px;border:3px solid var(--green)}
.contact-title{position:absolute;top:-14px;left:14px;right:14px;text-align:center;background:#f2f2f2;color:var(--blue);font-weight:500;font-size:18px}
.contact-lines{position:absolute;top:34px;left:12px;right:12px}
.contact-lines span{display:block;height:31px;border-bottom:1px dotted #c8c8c8}
.contact-tag{position:absolute;right:12px;bottom:12px;width:26px;height:26px;background:var(--green);border-radius:4px}

/* Cover */
.cover{background:#fff;display:flex;flex-direction:column}
.cover-head{height:78px;display:flex;flex-direction:column;align-items:flex-end;justify-content:center;padding-right:18px}
.cover-head .brand{font-size:30px}
.cover-head .brand-sub{font-size:22px;font-weight:400}
.people-grid{height:440px;background:linear-gradient(135deg,#e07a1f 0%,#8a3ab0 20%,#d62a2a 38%,#1f9be0 55%,#9bc23a 72%,#5a4ab8 88%,#c9a82a 100%)}
.cover-foot{flex:1;background:var(--grey-light);display:flex;flex-direction:column;align-items:center;justify-content:center;color:var(--blue);font-weight:500;font-size:12px;line-height:1.3}

/* Inside */
.inside-panel{padding-top:16px;text-align:center}
.unique{background:linear-gradient(#efefef,#fff 60%)}
.explain{background:#f4f4f4}
.benefits{background:#fff}
.panel-title{color:var(--blue);font-weight:500;font-size:18px}
.panel-title--green{color:var(--green);font-size:17px;line-height:1.1;padding:0 14px}
.steps{margin-top:16px;padding:0 12px}
.step{display:flex;align-items:center;gap:8px;height:71px}
.step--flip{flex-direction:row-reverse}
.step-text{flex:1;font-size:7.3px;line-height:1.25;color:#666}
.step-text b{font-weight:400;display:block}
.step-shot{width:64px;height:56px;background:linear-gradient(#e8eef5,#c9d6e3);border:2px solid #fff;box-shadow:0 1px 3px rgba(0,0,0,.3)}
.easy{position:absolute;left:60px;right:10px;bottom:16px;text-align:center}
.easy-title{color:var(--green);font-size:17px;font-weight:500}
.easy-text{color:var(--blue);font-size:9.5px;font-weight:500;line-height:1.25;margin-top:3px}
.easy-tag{position:absolute;left:8px;bottom:26px;width:34px;height:34px;border-radius:5px;background:var(--green)}

.explain-body{padding:14px 26px 0;font-size:8px;line-height:1.7;color:#666}
.explain-body p+p{margin-top:6px}
.explain .seal{left:88px;top:305px;width:70px;height:70px}
.photo-row{position:absolute;top:400px;left:16px;right:16px;display:flex;justify-content:space-between}
.photo-row span{width:62px;height:62px;border:3px solid #fff;box-shadow:0 1px 3px rgba(0,0,0,.3)}
.photo-row span:nth-child(1){background:linear-gradient(#eef0f2,#b9c0c8)}
.photo-row span:nth-child(2){background:linear-gradient(#8a9a7a,#3c3c30)}
.photo-row span:nth-child(3){background:linear-gradient(#e8d4c4,#6f8fb8)}
.explain-brand{position:absolute;left:0;right:0;bottom:18px;display:flex;flex-direction:column;align-items:center}
.explain-brand .brand{font-size:26px}
.explain-brand .brand-sub{font-size:20px;font-weight:400;align-self:flex-end;margin-right:40px}

.perks{display:flex;justify-content:space-around;margin-top:12px;padding:0 6px}
.perk{width:70px;font-size:8px;line-height:1.2;color:#555}
.perk svg{display:block;margin:0 auto 4px}
.receive{margin-top:10px}
.boxes{display:grid;grid-template-columns:repeat(3,60px);gap:12px 14px;justify-content:center;margin-top:10px}
.box{height:60px;background:var(--green);border:2px solid #fff;box-shadow:0 1px 3px rgba(0,0,0,.25);color:#d7efbf;font-size:7.5px;line-height:1.2;display:flex;align-items:center;justify-content:center;padding:2px}
.box--last{grid-column:3}
.couple-photo{position:absolute;left:0;right:0;bottom:0;height:160px;background:linear-gradient(160deg,#f1eee9 0%,#d8d0c6 45%,#9b8c80 100%);z-index:0}
.benefits .boxes{position:relative;z-index:1}
</style>
</head>
<body>

<section class="spread spread--outside">
  <div class="panel services">
    <div class="pill">AVAILABLE SERVICE</div>
    <div class="service">
      <div class="brand">Silver Harbor</div>
      <div class="brand-sub">Home Services</div>
    </div>
    <div class="pill">COMING SOON</div>
    <div class="service">
      <div class="brand">Silver Harbor</div>
      <div class="brand-sub">Auto Services</div>
    </div>
    <div class="service">
      <div class="brand">Silver Harbor</div>
      <div class="brand-sub">Life &amp; Learning</div>
    </div>
    <div class="sunset-photo" role="img" aria-label="Photo of a family driving an open-top car into the sunset"></div>
    <div class="seal" aria-hidden="true"></div>
  </div>

  <div class="panel contact">
    <div class="contact-frame">
      <div class="contact-title">Contact Information</div>
      <div class="contact-lines"><span></span><span></span><span></span><span></span><span></span><span></span><span></span><span></span><span></span><span></span><span></span><span></span><span></span><span></span></div>
      <div class="contact-tag" aria-hidden="true"></div>
    </div>
  </div>

  <div class="panel cover">
    <div class="cover-head">
      <div class="brand"><span class="brand-dot"></span>Silver Harbor</div>
      <div class="brand-sub">Circle</div>
    </div>
    <div class="people-grid" role="img" aria-label="Grid of smiling member portraits on bright coloured backgrounds"></div>
    <div class="cover-foot">
      <span>www.silverharborcircle.com</span>
      <span>www.silverharborhome.com</span>
    </div>
  </div>
</section>

<section class="spread spread--inside">
  <div class="panel inside-panel unique">
    <h2 class="panel-title">Unique Process</h2>
    <div class="steps">
      <div class="step"><p class="step-text"><b>Your Price is Accepted</b>Within 60 minutes, you will be notified when one of our service pros accepts your price. The service pro will then contact you directly to set up your appointment.</p><div class="step-shot" role="img" aria-label="Screenshot of the get started form"></div></div>
      <div class="step step--flip"><p class="step-text"><b>Your Price is Accepted</b>Within 60 minutes, you will be notified when one of our service pros accepts your price. The service pro will then contact you directly to set up your appointment.</p><div class="step-shot" role="img" aria-label="Screenshot of the symptom list"></div></div>
      <div class="step"><p class="step-text"><b>Your Price is Accepted</b>Within 60 minutes, you will be notified when one of our service pros accepts your price. The service pro will then contact you directly to set up your appointment.</p><div class="step-shot" role="img" aria-label="Screenshot of the estimated price"></div></div>
      <div class="step step--flip"><p class="step-text"><b>Your Price is Accepted</b>Within 60 minutes, you will be notified when one of our service pros accepts your price. The service pro will then contact you directly to set up your appointment.</p><div class="step-shot" role="img" aria-label="Screenshot of the price entry screen"></div></div>
      <div class="step"><p class="step-text"><b>Your Price is Accepted</b>Within 60 minutes, you will be notified when one of our service pros accepts your price. The service pro will then contact you directly to set up your appointment.</p><div class="step-shot" role="img" aria-label="Photo of a service pro greeting a homeowner"></div></div>
      <div class="step step--flip"><p class="step-text"><b>Your Price is Accepted</b>Within 60 minutes, you will be notified when one of our service pros accepts your price. The service pro will then contact you directly to set up your appointment.</p><div class="step-shot" role="img" aria-label="Photo of a relaxed person on a lawn"></div></div>
    </div>
    <div class="easy-tag" aria-hidden="true"></div>
    <div class="easy">
      <div class="easy-title">It's that easy!</div>
      <p class="easy-text">In a matter of minutes, you have found a reputable, qualified service pro to take care of your project – at a price that you selected!</p>
    </div>
  </div>

  <div class="panel inside-panel explain">
    <h2 class="panel-title">Explaining Process</h2>
    <div class="explain-body">
      <p>Silver Harbor Circle's innovative model combines the bulk savings idea of Bulkmart with the "name your own price" concept of Bidwell to fill provider vacancies.</p>
      <p>A win-win for consumers and service providers alike, Silver Harbor Circle empowers Member consumers with fair market rate information for home improvement, maintenance and repair services; and then enables them to name their own price to submit to a network of pre-screened, local service professionals who have vacancies in their schedules that they are willing to fill at the Member's submitted price.</p>
    </div>
    <div class="seal" aria-hidden="true"></div>
    <div class="photo-row">
      <span role="img" aria-label="Photo of a signed invoice"></span>
      <span role="img" aria-label="Photo of cash in hand"></span>
      <span role="img" aria-label="Photo of a couple with a piggy bank"></span>
    </div>
    <div class="explain-brand">
      <div class="brand"><span class="brand-dot"></span>Silver Harbor</div>
      <div class="brand-sub">Circle</div>
    </div>
  </div>

  <div class="panel inside-panel benefits">
    <h2 class="panel-title panel-title--green">Benefits of becoming a Silver Harbor Circle Promoter</h2>
    <div class="perks">
      <div class="perk">
        <svg width="40" height="40" viewBox="0 0 40 40" aria-hidden="true"><circle cx="20" cy="20" r="18" fill="none" stroke="var(--green)" stroke-width="2.5"/><rect x="11" y="14" width="18" height="13" rx="2" fill="var(--green)"/><rect x="22" y="18" width="7" height="5" fill="#fff"/></svg>
        Earn Residual Income</div>
      <div class="perk">
        <svg width="40" height="40" viewBox="0 0 40 40" aria-hidden="true"><circle cx="20" cy="20" r="18" fill="none" stroke="var(--green)" stroke-width="2.5"/><rect x="13" y="10" width="14" height="19" fill="none" stroke="var(--green)" stroke-width="2"/><path d="M16 15h8M16 19h8M16 23h5" stroke="var(--green)" stroke-width="1.5"/></svg>
        Reclaim Your Time</div>
      <div class="perk">
        <svg width="40" height="40" viewBox="0 0 40 40" aria-hidden="true"><circle cx="20" cy="20" r="18" fill="none" stroke="var(--green)" stroke-width="2.5"/><path d="M10 21l6-5 4 3 4-3 6 5-6 5-4-3-4 3z" fill="var(--green)"/></svg>
        Help People Save Money</div>
    </div>
    <h2 class="panel-title panel-title--green receive">When Becoming a Silver Harbor Circle Promoter you'll receive</h2>
    <div class="couple-photo" role="img" aria-label="Photo of a smiling senior couple using a laptop in their kitchen"></div>
    <div class="boxes">
      <div class="box">Personalized Replicated Website</div>
      <div class="box">Back Office Suite</div>
      <div class="box">Personal Earnings Report</div>
      <div class="box">Marketing Tools</div>
      <div class="box">Team Telemetry</div>
      <div class="box">Sales Training</div>
      <div class="box box--last">Technical Support</div>
    </div>
  </div>
</section>

</body>
</html>
```